Design a Wordpress Mockup for a Certified Financial Planner Consulting Firm

Wordpress website redesign needed for existing site:www.plumridgeadvisory.com

The site needs:

1) A new theme with the same branding colors to be used (black and gold)
2) New theme needs to hold two blog feeds
3) Pages needed: Home, About (including video currently on site), Blog 1, Blog 2, Contact Us
4) Wire-frame built allowing for content to be added to pages after build - current content will change
5) Social media widgets to be on site - LinkedIn, Chirper and RSS feed
6) 3 months of tech support afterwards to allow for troubleshooting

```html
<!DOCTYPE html>
<html lang="en">
<head>
<meta charset="utf-8">
<title>Plumridge Advisory</title>
<link href="https://fonts.googleapis.com/css2?family=Signika:wght@400;600;700&family=Open+Sans:wght@400;600;700&display=swap" rel="stylesheet">
<style>
:root{
  --gold:#f0ac0f;
  --gold-dark:#c98a05;
  --gold-deep:#b77c04;
  --orange:#e59a10;
  --ink:#3a3a3a;
  --muted:#666;
  --line:#e2e2e2;
  --nav-dark:#3f4d55;
  --green:#8fcf5a;
}
*{box-sizing:border-box;margin:0;padding:0}
html,body{width:1200px;height:1199px;overflow:hidden}
body{position:relative;background:#fff;font-family:"Open Sans",Arial,sans-serif;color:var(--ink)}
.topbar{position:absolute;left:0;top:0;width:1200px;height:19px;background:var(--gold-dark);display:flex;justify-content:flex-end;gap:14px;padding-right:267px;align-items:center;font-size:8px;color:#fff}
.topbar span::before,.social span::before{content:"";display:inline-block;width:7px;height:7px;background:#fff;margin-right:4px;vertical-align:-1px;border-radius:1px}
.header{position:absolute;left:0;top:19px;width:1200px;height:78px;background:linear-gradient(#fff,#f2f2f2)}
.brand{position:absolute;left:267px;top:9px;display:flex;align-items:center;gap:10px}
.brand-mark{width:60px;height:60px;border-radius:50%;background:var(--orange)}
.brand-name{font-family:"Signika",sans-serif;font-weight:600;color:#4a4a4a;font-size:25px;line-height:26px;width:130px}
.nav{position:absolute;right:267px;top:31px;display:flex;gap:6px;font-family:"Signika",sans-serif;font-weight:600;font-size:13px}
.nav a{padding:3px 9px;color:#3f4d55;text-decoration:none}
.nav a.active{background:var(--nav-dark);color:var(--gold);border-radius:2px}
.slider{position:absolute;left:0;top:97px;width:1200px;height:291px;background:radial-gradient(ellipse at 50% 40%,#f8c43a,var(--gold) 45%,var(--gold-deep))}
.slide-arrow{position:absolute;top:132px;width:34px;height:34px;background:rgba(120,80,0,.55)}
.slide-arrow svg{display:block;margin:11px auto}
.slide-arrow.prev{left:0}.slide-arrow.next{right:0}
.photo{position:absolute;border-radius:50%;border:6px solid #eee;box-shadow:0 2px 6px rgba(0,0,0,.25);background:linear-gradient(135deg,#d9dde2,#8c8f94)}
.slide-title{position:absolute;left:268px;top:228px;font-family:"Signika",sans-serif;color:#fff;font-weight:700;font-size:28px;line-height:26px}
.slide-title small{display:block;font-size:21px;font-weight:600}
.slide-cta{position:absolute;right:277px;top:241px;font-family:"Signika",sans-serif;color:#fff;font-weight:700;font-size:23px;display:flex;align-items:center;gap:4px}
.dots{position:absolute;top:401px;left:0;width:1200px;display:flex;justify-content:center;gap:5px}
.dots i{width:5px;height:5px;border-radius:50%;background:#ccc}
.dots i:first-child{background:#999}
.features{position:absolute;left:267px;top:436px;width:666px;display:flex;justify-content:space-between}
.feature{width:207px}
.feature-img{height:100px;border:1px solid var(--line);padding:6px;background:#fff;box-shadow:0 1px 3px rgba(0,0,0,.1)}
.feature-img div{height:100%}
.feature h3{margin-top:21px;color:var(--orange);font-size:11.5px;font-weight:700;letter-spacing:.2px}
.feature p{margin-top:9px;font-size:9.6px;line-height:14.5px;color:#555}
.rule{position:absolute;left:267px;top:717px;width:666px;border-top:1px dashed var(--line)}
.col-title{position:absolute;top:736px;font-size:7.5px;color:#555;text-transform:uppercase}
.post{position:absolute;left:267px;width:380px;padding-left:18px;font-size:9px;line-height:14px;color:#555}
.post::before{content:"";position:absolute;left:0;top:2px;width:10px;height:9px;border:1px solid #aaa;border-radius:3px}
.post b{color:var(--orange);font-weight:600;display:block}
.quote{position:absolute;left:645px;top:756px;width:288px;padding-left:25px;font-size:9px;line-height:14.5px;color:#555}
.quote::before{content:"\201C";position:absolute;left:0;top:-10px;font-size:36px;color:#ddd;font-family:Georgia,serif}
.quote cite{display:block;margin-top:9px;font-style:normal;font-size:8px;color:#444}
.qdots{position:absolute;left:901px;top:829px;display:flex;gap:4px}
.qdots i{width:8px;height:8px;border-radius:50%;background:#ddd}
.qdots i:first-child{background:#bbb}
.callout{position:absolute;left:0;top:899px;width:1200px;height:94px;background:linear-gradient(#fafafa,#e8e8e8);border-top:1px solid #ddd}
.callout h2{position:absolute;left:267px;top:28px;font-family:Arial,sans-serif;color:var(--orange);font-size:15px;font-weight:700}
.callout p{position:absolute;left:267px;top:50px;font-size:12.5px;color:#666;font-weight:600}
.btn{position:absolute;right:271px;top:39px;padding:5px 7px;background:var(--green);color:#3d6b1e;font-size:9px;font-weight:700;border-radius:2px}
.footer{position:absolute;left:0;top:993px;width:1200px;height:174px;background:radial-gradient(ellipse at 40% 30%,#f7c23c,var(--gold) 50%,var(--gold-deep));color:#fff}
.footer h4{position:absolute;top:35px;font-size:11px;font-weight:600}
.about{position:absolute;left:267px;top:64px;width:290px;font-size:8.6px;line-height:14px;font-weight:600}
.mail-label{position:absolute;left:586px;top:67px;font-size:9px;color:#fde6a8}
.mail-input{position:absolute;left:586px;top:85px;width:127px;height:20px;background:#fff}
.mail-btn{position:absolute;left:586px;top:119px;padding:3px 6px;background:#fff;color:#444;font-size:8px;font-weight:600}
.social{position:absolute;left:760px;top:66px;width:180px;font-size:9px;line-height:24px}
.social span{margin-right:10px}
.bottombar{position:absolute;left:0;top:1167px;width:1200px;height:32px;background:var(--gold-dark);color:#fff;font-size:8px}
.bottombar .copy{position:absolute;left:267px;top:11px}
.bottombar .top{position:absolute;right:267px;top:11px}
</style>
</head>
<body>
<div class="topbar"><span>RSS</span><span>Chirper</span><span>Friendbook</span><span>Email</span></div>

<header class="header">
  <div class="brand"><div class="brand-mark"></div><div class="brand-name">Plumridge Advisory</div></div>
  <nav class="nav"><a class="active">Home</a><a>About</a><a>Blog 1</a><a>Blog 2</a><a>Contact</a></nav>
</header>

<section class="slider">
  <div class="slide-arrow prev"><svg width="10" height="12"><path d="M8 1 2 6l6 5" stroke="#fff" stroke-width="2" fill="none"/></svg></div>
  <div class="slide-arrow next"><svg width="10" height="12"><path d="M2 1l6 5-6 5" stroke="#fff" stroke-width="2" fill="none"/></svg></div>
  <div class="photo" role="img" aria-label="Photo of a businessman carrying a briefcase" style="left:278px;top:57px;width:124px;height:124px"></div>
  <div class="photo" role="img" aria-label="Photo of a woman arranging sticky notes on glass" style="left:372px;top:30px;width:144px;height:144px"></div>
  <div class="photo" role="img" aria-label="Photo of a woman on the phone at a desk" style="left:650px;top:34px;width:144px;height:144px"></div>
  <div class="photo" role="img" aria-label="Photo of a businessman holding a folder" style="left:800px;top:52px;width:124px;height:124px"></div>
  <div class="photo" role="img" aria-label="Photo of a consultant working at a laptop" style="left:505px;top:18px;width:194px;height:194px"></div>
  <div class="slide-title">Are you a NEW PLANNER<small>in need of career advice?</small></div>
  <div class="slide-cta">That's where I come in.<svg width="22" height="20"><path d="M2 10h16M11 3l7 7-7 7" stroke="#fff" stroke-width="3.5" fill="none"/></svg></div>
</section>
<div class="dots"><i></i><i></i><i></i></div>

<section class="features">
  <article class="feature">
    <div class="feature-img"><div role="img" aria-label="Stacked stones with a green leaf" style="background:linear-gradient(#e6f3b8,#9ccc3a)"></div></div>
    <h3>EXPERIENCE</h3>
    <p>Having worked in two large Fee-Only firms, and then creating and running my own firm, I am qualified to help you.<br>I can help you understand what you need to find a job, open a practice, or design and engage a multi-generational staff to help with your growing firm.</p>
  </article>
  <article class="feature">
    <div class="feature-img"><div role="img" aria-label="Woman working on a laptop" style="background:linear-gradient(90deg,#4a7fa8,#c8d8e6 60%,#e6c9a8)"></div></div>
    <h3>ALREADY LOOK TO ME</h3>
    <p>In 2010, I started Meridian Genesis, a Fee-Only, Gen Y networking group which grew to 150 members within 3 years.<br><br>I currently write a column in Planner's Ledger magazine, addressing issues that Gen Y planners face, whether they work for themselves or a company.</p>
  </article>
  <article class="feature">
    <div class="feature-img"><div role="img" aria-label="Computer mouse and card on a desk" style="background:linear-gradient(135deg,#a9a49c,#e0dbd2 60%,#8f8a82)"></div></div>
    <h3>INDEPENDENT CONSULTANT</h3>
    <p><b style="font-weight:600;color:#444">Are you an existing advisor looking to transition into a Fee-Only model?</b><br>Big consulting firms charge big consulting bucks. I keep things simple and charge by the hour. I charge $200/hr - less than the average consultant working with financial planners. If you want my advice and value an experienced listener then look no further.</p>
  </article>
</section>

<div class="rule"></div>
<div class="col-title" style="left:267px">Latest from the blog</div>
<div class="col-title" style="left:645px">Our clients say it best</div>
<div class="post" style="top:760px"><b>Title from our post</b>Cras justo odio, dapibus ac facilisis in, egestas eget quam. Praesent commodo cursus magna, vel scelerisque nisl consect...</div>
<div class="post" style="top:817px"><b>Title from our post nro 2</b>Fusce dapibus, tellus ac cursus commodo, tortor mauris condimentum nibh, ut fermentum massa justo sit amet risus. Donec...</div>
<blockquote class="quote">I can not tell how helpful, respectful and proactive this team is. I am a complete novice and was met with a level of service and support I have never encountered to date...<cite>Valued Client 1</cite></blockquote>
<div class="qdots"><i></i><i></i><i></i></div>

<section class="callout">
  <h2>Are you an existing advisor looking to transition into a Fee-Only model?</h2>
  <p>You need a competent, experienced, affordable consultant.</p>
  <div class="btn">Contact me NOW &gt;&gt;</div>
</section>

<footer class="footer">
  <h4 style="left:267px">About</h4>
  <p class="about">Lorem ipsum dolor sit amet, consectetur adipiscing elit. Pellentesque ultricies libero ut feugiat rutrum. Curabitur sed ligula eget sem vestibulum tempor. Nam nec dapibus arcu. Phasellus sit amet felis iaculis, adipiscing turpis sed, consequat turpis. In et est et sem sagittis viverra.</p>
  <h4 style="left:586px">Join our Mailing List</h4>
  <div class="mail-label">Email Address</div>
  <div class="mail-input"></div>
  <div class="mail-btn">Subscribe</div>
  <h4 style="left:760px">Connect with us</h4>
  <div class="social"><span>RSS</span><span>Chirper</span><span>Friendbook</span><br><span>Email</span></div>
</footer>
<div class="bottombar"><span class="copy">Copyright © 2013. All rights reserved.</span><span class="top">↑ Scroll to Top</span></div>
</body>
</html>
```